Paws Forward Academy Business card design

We need a business card for our Dog Training business which is based in the Australian Region of ACT region and surrounds.

We offer a variety of services from group classes in socialisation and obedience training, home visits addressing individual training and behaviour issues.

We also trial and on sell and promote pet products especially specific training and health products for dogs.

We promote responsible pet onwership through supporting adopted dogs through rescue associations and actively assisting and promoting various campaigns hence being the ACT Representative for the Southern Bluecollar Hound Initiative.
Updates

Looking at current designs that have focussed on making the business's Logo the hero of the branding and marketting.

Delete the: Owner/Trainer

Reason: Still refining current top designs and getting marketting feedback from friends and business managers

Please ensure the 3 lines of details if included is the following;

Professional Dog Training

Dog Behaviour Consultation

Pet Product Sales / Advice

If possible can we add the facebook link in the contact information

facebook.com/PFPupCrew

Target Market(s)

Families and Individuals who are pet dog owners aged 17 to 95 that need support or advice on training and behaviour issues

Industry/Entity Type

Training

Contact Information for Business Card

Paws Forward Academy
Mitchell Kerrane
Owner / Trainer

Professional Dog Training

0431 786 254
info@pawsforwardhq.com.au
www.pawsforwardhq.com.au

Logo styles of interest
Character Logo
Requirements
Must have
• The Paws Forward Academy LOGO incorporated into the card as the Brand representation. Promote and market the logo as the brand.

```html
<!DOCTYPE html>
<html lang="en">
<head>
<meta charset="utf-8">
<title>Paws Forward Academy – Business Card</title>
<link rel="stylesheet" href="https://fonts.googleapis.com/css2?family=Open+Sans:wght@400;600;700&display=swap">
<style>
  :root {
    --canvas: #e9ecef;
    --card-white: #ffffff;
    --ink-grey: #6f7175;
    --brand-blue: #1f7fd6;
    --band-blue: #7fa6e0;
    --band-text: #ffffff;
    --back-light: #63b3ea;
    --back-deep: #0d62c9;
    --back-text: #eef5ff;
  }
  * { box-sizing: border-box; margin: 0; padding: 0; }
  html, body {
    width: 1200px; height: 1000px; overflow: hidden;
    background: var(--canvas);
    font-family: "Open Sans", Arial, sans-serif;
  }
  .canvas { position: relative; width: 1200px; height: 1000px; }

  .card {
    position: absolute; width: 580px; height: 330px;
    border-radius: 4px; overflow: hidden;
    box-shadow: 0 6px 18px rgba(0,0,0,.18);
  }

  /* Front */
  .card-front { left: 70px; top: 110px; background: var(--card-white); }
  .brand {
    position: absolute; left: 0; right: 0; top: 70px;
    display: flex; align-items: center; justify-content: center; gap: 14px;
  }
  .brand-dot { width: 22px; height: 22px; border-radius: 50%; background: var(--brand-blue); flex: none; }
  .brand-name {
    font-size: 34px; font-weight: 600; color: var(--ink-grey); letter-spacing: .5px;
    white-space: nowrap;
  }
  .person { position: absolute; left: 0; right: 0; top: 162px; text-align: center; }
  .person-name { font-size: 24px; font-weight: 700; color: var(--ink-grey); }

  .contact-band {
    position: absolute; left: 0; right: 0; top: 236px; height: 66px;
    background: var(--band-blue);
    display: grid; grid-template-columns: 1fr 1fr; align-content: center;
    row-gap: 8px; column-gap: 20px;
    padding: 0 34px; color: var(--band-text); font-size: 13px;
  }
  .contact-item { display: flex; align-items: center; gap: 7px; white-space: nowrap; }
  .contact-item svg { width: 14px; height: 14px; flex: none; fill: none; stroke: var(--band-text); stroke-width: 1.6; }

  /* Back */
  .card-back {
    left: 550px; top: 560px;
    background: radial-gradient(ellipse at 20% 10%, var(--back-light) 0%, var(--brand-blue) 45%, var(--back-deep) 100%);
  }
  .services {
    position: absolute; right: 28px; top: 26px;
    border-left: 1.5px solid var(--back-text);
    padding-left: 8px; color: var(--back-text);
    font-size: 12px; line-height: 1.4;
  }
  .back-brand {
    position: absolute; left: 34px; bottom: 44px;
    display: flex; align-items: center; gap: 16px;
  }
  .back-brand .brand-dot { width: 30px; height: 30px; background: var(--back-text); }
  .back-brand .brand-name { font-size: 40px; color: var(--back-text); }
</style>
</head>
<body>
<main class="canvas">

  <section class="card card-front" aria-label="Business card front">
    <div class="brand">
      <span class="brand-dot"></span>
      <span class="brand-name">Paws Forward Academy</span>
    </div>
    <div class="person">
      <p class="person-name">Mitchell Kerrane</p>
    </div>
    <div class="contact-band">
      <span class="contact-item">
        <svg viewBox="0 0 16 16"><path d="M4 2l2.5 3-1.5 1.5c1 2 2.5 3.5 4.5 4.5L11 9.5l3 2.5-1.5 2C7 14 2 9 2 3.5z"/></svg>
        0431 786 254
      </span>
      <span class="contact-item">
        <svg viewBox="0 0 16 16"><circle cx="8" cy="8" r="2.5"/><path d="M10.5 8v1.2c0 1.2 2.5 1.2 2.5-1.2A5 5 0 1 0 11 12"/></svg>
        info@pawsforwardhq.com.au
      </span>
      <span class="contact-item">
        <svg viewBox="0 0 16 16"><path d="M2.5 3h11v7.5h-6l-3 3v-3h-2z"/></svg>
        facebook.com/PFPupCrew
      </span>
      <span class="contact-item">
        <svg viewBox="0 0 16 16"><path d="M3.5 1.5h6l3 3v10h-9z"/><path d="M5.5 8h5M5.5 10.5h5"/></svg>
        www.pawsforwardhq.com.au
      </span>
    </div>
  </section>

  <section class="card card-back" aria-label="Business card back">
    <div class="services">
      <p>Professional Dog Training</p>
      <p>Dog Behaviour Consultation</p>
      <p>Pet Product Sales / Advice</p>
    </div>
    <div class="back-brand">
      <span class="brand-dot"></span>
      <span class="brand-name">Paws Forward Academy</span>
    </div>
  </section>

</main>
</body>
</html>
```